Waffle Poster Design

Need a A1 size poster (VERTICAL POSTER) to introduce Belgian waffle sandwich. Price is from $6 each. Waffle looks like the attached file. it has different spreads/filling. I found the attached file online, hence the picture quality is not good for an A1 size poster.

```html
<!DOCTYPE html>
<html lang="en">
<head>
<meta charset="utf-8">
<title>Belgian Waffle Sandwich Poster</title>
<link rel="stylesheet" href="https://fonts.googleapis.com/css2?family=Kaushan+Script&family=Oswald:wght@500;600;700&family=Open+Sans:wght@700;800&display=swap">
<style>
  :root {
    --brown: #5a3320;
    --red: #b2382c;
    --paper: #f2f2f2;
    --paper-shade: #e6e6e6;
    --band: #dedede;
    --photo-light: #e2b98a;
    --photo-mid: #cf9a62;
    --photo-dark: #b07a45;
  }
  html, body {
    margin: 0;
    padding: 0;
    overflow: hidden;
    background: var(--paper);
  }
  .poster {
    position: relative;
    width: 923px;
    height: 1200px;
    overflow: hidden;
    background: linear-gradient(180deg, var(--paper) 0%, #f7f7f7 45%, var(--paper-shade) 100%);
    color: var(--brown);
    font-family: "Open Sans", Arial, sans-serif;
  }
  .header-band {
    position: absolute;
    left: 0; top: 0;
    width: 923px; height: 300px;
  }
  .title {
    position: absolute;
    left: 0; right: 0; top: 8px;
    margin: 0;
    text-align: center;
    font-family: "Kaushan Script", cursive;
    font-weight: 400;
    font-size: 138px;
    line-height: 1.1;
    color: var(--brown);
    letter-spacing: -2px;
    white-space: nowrap;
  }
  .subtitle {
    position: absolute;
    left: 0; right: 0; top: 162px;
    text-align: center;
    font-family: "Oswald", sans-serif;
    font-weight: 600;
    font-size: 74px;
    line-height: 1;
    color: var(--red);
    letter-spacing: 1px;
  }
  .subtitle .dots {
    font-size: 40px;
    vertical-align: 14px;
    letter-spacing: 4px;
  }
  .price-badge {
    position: absolute;
    left: 35px; top: 311px;
    width: 236px; height: 236px;
  }
  .price-text {
    position: absolute;
    left: 35px; top: 311px;
    width: 236px; height: 236px;
    transform: rotate(-8deg);
    text-align: center;
    font-family: "Oswald", sans-serif;
    font-weight: 700;
  }
  .price-text .amount {
    display: block;
    margin-top: 38px;
    font-size: 92px;
    line-height: 1;
    color: var(--red);
  }
  .price-text .unit {
    display: block;
    font-size: 52px;
    line-height: 1;
    color: var(--brown);
  }
  .menu-heading {
    position: absolute;
    margin: 0;
    font-family: "Oswald", sans-serif;
    font-weight: 600;
    text-transform: uppercase;
    line-height: 1;
    color: var(--brown);
    white-space: nowrap;
  }
  .menu-heading .accent { color: var(--red); }
  .heading-simple { left: 380px; top: 346px; font-size: 58px; }
  .heading-combo { left: 190px; top: 560px; font-size: 62px; }
  .rule {
    position: absolute;
    height: 2px;
    background: var(--brown);
  }
  .rule-simple { left: 808px; top: 381px; width: 115px; }
  .rule-combo { left: 0; top: 594px; width: 165px; }
  .menu-list {
    position: absolute;
    margin: 0;
    padding: 0;
    list-style: none;
    text-align: center;
    font-weight: 800;
    font-size: 21.5px;
    line-height: 29.5px;
    color: var(--brown);
    white-space: nowrap;
  }
  .list-simple { left: 318px; width: 540px; top: 410px; }
  .list-combo { left: 80px; width: 780px; top: 632px; }
  .topping-box {
    position: absolute;
    left: 94px; top: 792px;
    width: 273px; height: 116px;
    box-sizing: border-box;
    border: 2px solid var(--brown);
    padding: 5px;
  }
  .topping-inner {
    height: 100%;
    box-sizing: border-box;
    border: 2px dotted var(--brown);
    text-align: center;
    padding-top: 14px;
  }
  .topping-main {
    display: block;
    font-family: "Oswald", sans-serif;
    font-weight: 600;
    font-size: 36px;
    line-height: 1;
    color: var(--brown);
  }
  .topping-main .accent { color: var(--red); }
  .topping-note {
    display: block;
    font-family: "Kaushan Script", cursive;
    font-size: 22px;
    line-height: 1.3;
    color: var(--red);
  }
  .product-photo {
    position: absolute;
    left: 392px; top: 776px;
    width: 531px; height: 364px;
    background: linear-gradient(160deg, var(--photo-light) 0%, var(--photo-mid) 55%, var(--photo-dark) 100%);
  }
</style>
</head>
<body>
<main class="poster">
  <svg class="header-band" viewBox="0 0 923 300" aria-hidden="true">
    <path d="M0 0 H923 V256 Q461 330 0 256 Z" fill="var(--band)"/>
  </svg>

  <h1 class="title">Belgian Waffle</h1>
  <div class="subtitle"><span class="dots">•••</span> SANDWICH <span class="dots">•••</span></div>

  <svg class="price-badge" viewBox="0 0 236 236" aria-hidden="true">
    <circle cx="118" cy="118" r="115" fill="none" stroke="var(--brown)" stroke-width="3"/>
    <circle cx="118" cy="118" r="103" fill="none" stroke="var(--brown)" stroke-width="2.5" stroke-dasharray="1 6" stroke-linecap="round"/>
  </svg>
  <div class="price-text">
    <span class="amount">$6</span>
    <span class="unit">EACH</span>
  </div>

  <h2 class="menu-heading heading-simple">Simply <span class="accent">Perfect!</span></h2>
  <div class="rule rule-simple"></div>
  <ul class="menu-list list-simple">
    <li>Chocolate • Peanut Butter • Strawberry Coulis</li>
    <li>Nuttora • Blueberry • Cream Cheese</li>
    <li>Condensed Milk • Raspberry Coulis</li>
  </ul>

  <div class="rule rule-combo"></div>
  <h2 class="menu-heading heading-combo"><span class="accent">Perfect</span> Combination</h2>
  <ul class="menu-list list-combo">
    <li>Ham &amp; Cheddar • Banana Peanut Butter • Banana Chocolate</li>
    <li>Chocolate Peanut Butter • Banana Hazelnut • Ham &amp; Creamcheese</li>
    <li>Blueberry Creamcheese • Strawberry Creamcheese</li>
  </ul>

  <div class="topping-box">
    <div class="topping-inner">
      <span class="topping-main">JUST ADD <span class="accent">$1</span></span>
      <span class="topping-note">for extra topping!</span>
    </div>
  </div>

  <div class="product-photo" role="img" aria-label="Photo of two golden Belgian waffle sandwiches filled with blueberry jam and peanut butter"></div>
</main>
</body>
</html>
```